ultra-minimalist business card

front (black background, matte):

samir t. kouri
writer | photographer
get@samirkouri.com

back (white background, matte):

a picture speaks a thousand words;
a word draws a thousand pictures.

www.samirkouri.com

all text should be small (white or silver - as long as it shows against the black - on the front; black or gray - as long as it shows against the white - on the back).

feel free to get creative in terms of arrangement, alignment, and font type, but remember, the overall style is minimalist, so nothing too fancy, please.

thanks.

```html
<!DOCTYPE html>
<html lang="en">
<head>
<meta charset="utf-8">
<title>Samir T. Kouri — Business Card Front</title>
<link rel="stylesheet" href="https://fonts.googleapis.com/css2?family=Gochi+Hand&family=Roboto+Condensed:wght@300&family=Roboto:wght@700&display=swap">
<style>
  :root {
    --card-black: #000000;
    --ink-white: #ffffff;
  }
  html, body {
    margin: 0;
    padding: 0;
    width: 1200px;
    height: 632px;
    overflow: hidden;
    background: var(--card-black);
  }
  .card-front {
    position: relative;
    width: 1200px;
    height: 632px;
    background: var(--card-black);
    color: var(--ink-white);
  }
  .frame-lines {
    position: absolute;
    inset: 0;
  }
  .card-text {
    position: absolute;
    left: 0;
    width: 100%;
    margin: 0;
    text-align: center;
    white-space: nowrap;
  }
  .name {
    top: 208px;
    font-family: "Gochi Hand", cursive;
    font-size: 58px;
    line-height: 1;
    letter-spacing: 2px;
  }
  .roles {
    top: 278px;
    font-family: "Roboto Condensed", sans-serif;
    font-weight: 300;
    font-size: 41px;
    line-height: 1;
  }
  .email {
    top: 380px;
    font-family: "Roboto", sans-serif;
    font-weight: 700;
    font-size: 42px;
    line-height: 1;
  }
</style>
</head>
<body>
  <main class="card-front">
    <svg class="frame-lines" width="1200" height="632" viewBox="0 0 1200 632" aria-hidden="true">
      <g fill="none" stroke="var(--ink-white)">
        <rect x="151" y="151" width="899" height="330" stroke-width="2"/>
        <rect x="158" y="158" width="885" height="316" stroke-width="3"/>
        <rect x="169.5" y="169.5" width="862" height="292" stroke-width="3"/>
      </g>
    </svg>
    <h1 class="card-text name">samir t. kouri</h1>
    <p class="card-text roles">writer | photographer</p>
    <p class="card-text email">get@samirkouri.com</p>
  </main>
</body>
</html>
```